New Webpage for High Class Expert Witness Services Company

We are looking for a minimalist design for a webpage that just has our logo and an entry form offer to connect with one of our Liaisons.
The entry form should just ask for Name, Email, Contact Info and Description of Project.

Company Name is: The Marlow Crest Advisory Services

Number of Pages Required

1 page

```html
<!DOCTYPE html>
<html lang="en">
<head>
<meta charset="UTF-8">
<title>Marlow Crest Advisory Services — Connect with a Liaison</title>
<link href="https://fonts.googleapis.com/css2?family=Cinzel:wght@600;700&family=Poppins:wght@400&display=swap" rel="stylesheet">
<style>
  :root {
    --ink-light: #ffffff;
    --ink-dark: #1c1c1c;
    --field-fill: rgba(190, 190, 190, 0.55);
    --field-edge: rgba(255, 255, 255, 0.75);
    --rule: rgba(255, 255, 255, 0.35);
    --scene-deep: #1d2a22;
    --scene-mid: #3b4a3c;
    --scene-warm: #6a4a2c;
    --scene-khaki: #8a7a5c;
    --brand-box: #151515;
  }
  * { box-sizing: border-box; margin: 0; padding: 0; }
  html, body { width: 1200px; height: 731px; overflow: hidden; }
  body { font-family: "Poppins", sans-serif; color: var(--ink-light); }
  .page { position: relative; width: 1200px; height: 731px; overflow: hidden; }
  .backdrop {
    position: absolute; inset: 0;
    background:
      radial-gradient(ellipse 260px 360px at 960px 420px, var(--scene-khaki) 0%, rgba(138,122,92,0.55) 45%, transparent 75%),
      radial-gradient(ellipse 500px 260px at 250px 640px, var(--scene-warm) 0%, transparent 70%),
      radial-gradient(ellipse 600px 400px at 550px 120px, #4f6656 0%, transparent 70%),
      linear-gradient(180deg, var(--scene-mid) 0%, var(--scene-deep) 60%, #2a2218 100%);
  }
  .brand {
    position: absolute; left: 138px; top: 34px; width: 318px; height: 57px;
    background: var(--brand-box);
    display: flex; align-items: center; gap: 12px; padding: 0 14px;
  }
  .brand-mark { width: 22px; height: 22px; background: var(--ink-light); flex: none; }
  .brand-name {
    font-family: "Cinzel", serif; font-weight: 600; font-size: 16px;
    letter-spacing: 0.5px; line-height: 1.15; color: var(--ink-light);
  }
  .heading {
    position: absolute; left: 143px; top: 173px;
    font-family: "Cinzel", serif; font-weight: 700; font-size: 35px;
    letter-spacing: 0.5px; white-space: nowrap;
  }
  .field-label {
    position: absolute; display: flex; align-items: center; gap: 11px;
    font-size: 13px; line-height: 1;
  }
  .field-label svg { width: 14px; height: 14px; fill: var(--ink-light); }
  .field {
    position: absolute; height: 43px;
    background: var(--field-fill); border: 1px solid var(--field-edge); border-radius: 2px;
  }
  .field-area { height: 89px; }
  .submit {
    position: absolute; left: 142px; top: 547px; width: 335px; height: 42px;
    background: var(--ink-light); color: var(--ink-dark); border: none; border-radius: 2px;
    font-family: "Cinzel", serif; font-weight: 700; font-size: 16px; letter-spacing: 0.3px;
  }
  .footer-rule { position: absolute; left: 0; right: 0; top: 676px; height: 1px; background: var(--rule); }
  .footer-note {
    position: absolute; left: 0; right: 0; top: 694px; text-align: center;
    font-size: 12.5px; color: var(--ink-light);
  }
</style>
</head>
<body>
<main class="page">
  <div class="backdrop" role="img" aria-label="Blurred autumn forest photograph with a masked soldier in tactical gear holding a rifle on the right"></div>

  <div class="brand">
    <span class="brand-mark"></span>
    <span class="brand-name">Marlow Crest<br>Advisory Services</span>
  </div>

  <h1 class="heading">CONNECT WITH A LIAISON</h1>

  <form>
    <label class="field-label" style="left:153px; top:255px;">
      <svg viewBox="0 0 16 16"><circle cx="8" cy="4.5" r="3.5"/><path d="M1.5 16c0-4 3-6.5 6.5-6.5s6.5 2.5 6.5 6.5z"/></svg>First Name
    </label>
    <div class="field" style="left:141px; top:275px; width:284px;"></div>

    <label class="field-label" style="left:447px; top:255px;">
      <svg viewBox="0 0 16 16"><circle cx="8" cy="4.5" r="3.5"/><path d="M1.5 16c0-4 3-6.5 6.5-6.5s6.5 2.5 6.5 6.5z"/></svg>Last Name
    </label>
    <div class="field" style="left:436px; top:275px; width:284px;"></div>

    <label class="field-label" style="left:153px; top:335px;">
      <svg viewBox="0 0 16 16"><path d="M16 1 0 7.5l5 2 1.5 5.5 2.5-3.5 4 3z"/></svg>Email Address
    </label>
    <div class="field" style="left:141px; top:354px; width:284px;"></div>

    <label class="field-label" style="left:447px; top:335px;">
      <svg viewBox="0 0 16 16"><path d="M3.5 1 1 3.5c0 6 5.5 11.5 11.5 11.5L15 12.5l-3-2.5-2 1.5C8 10.5 5.5 8 4.5 6l1.5-2z"/><path d="M9 1a6 6 0 0 1 6 6h-1.3A4.7 4.7 0 0 0 9 2.3zM9 3.6A3.4 3.4 0 0 1 12.4 7h-1.3A2.1 2.1 0 0 0 9 4.9z"/></svg>Contact info (phone / secure line)
    </label>
    <div class="field" style="left:436px; top:354px; width:284px;"></div>

    <label class="field-label" style="left:153px; top:415px;">
      <svg viewBox="0 0 16 16"><path d="M2 2h9v4l-4 4-.5 3.5L10 13l1-1v3H2zM4 4.5h5v1H4zm0 2.5h4v1H4zm0 2.5h2.5v1H4z"/><path d="M13.5 5.5 15 7l-6 6-2 .5.5-2z"/></svg>Description of Project
    </label>
    <div class="field field-area" style="left:141px; top:434px; width:579px;"></div>

    <button type="button" class="submit">REQUEST LIAISON CONNECTION</button>
  </form>

  <div class="footer-rule"></div>
  <p class="footer-note">© The Marlow Crest Advisory Services — Secure Liaison Protocol | All Submissions Encrypted</p>
</main>
</body>
</html>
```